Modern, pro female massage business needs business card design

We are a boutique, pro women's sports and remedial massage studio based in Singapore - we have a logo already (see attached image) and need to design a business card that reflects an elegant, modern and feminine feel using this logo.

We are focussed on a very local market and need to give a professional yet warm feeling.

Details for the card include (layout of your choice):

Talvina Brisk
Call, SMS or ChatBeam: 8317 6092
Email: tealmarrow@quenfold.com
Address: The Harbourview at Dunmore
82 Dunmore Road, East Coast, Singapore

To incorporate the OVAR logo (www.ovarglobe.co.uk) would be appreciated - see attached file.

Industry/Entity Type

Massage

Requirements
Nice to have
• We like the idea of using an embossed style card. Solid colour on the reverse - embossed on the front; four colour printing is okay.
Should not have
• It should not be uber 'girly girl' if that makes any sense. The logo is already colourful

```html
<!DOCTYPE html>
<html lang="en">
<head>
<meta charset="utf-8">
<title>tealmarrow – business cards</title>
<link rel="stylesheet" href="https://fonts.googleapis.com/css2?family=Arimo:wght@400;700&family=Cabin:wght@400&display=swap">
<style>
  :root {
    --brand-pink: #e0177f;
    --brand-green: #8dc63f;
    --soft-pink: #f4bcd9;
    --badge-blue: #1f6fb2;
    --ink: #1e1e1e;
    --tagline-grey: #4a4a4a;
    --card-white: #fdfdfd;
    --backdrop: #e9e8e5;
  }
  * { box-sizing: border-box; margin: 0; padding: 0; }
  html, body {
    width: 1200px;
    height: 980px;
    overflow: hidden;
    background: var(--backdrop);
  }
  .stage { position: relative; width: 1200px; height: 980px; }

  .card {
    position: absolute;
    width: 640px;
    height: 366px;
    background: var(--card-white);
    box-shadow: 0 6px 18px rgba(0,0,0,0.18);
    overflow: hidden;
  }
  .card--front { left: 90px; top: 70px; }
  .card--back  { left: 470px; top: 520px; }

  .wordmark {
    position: absolute;
    font-family: "Arimo", Arial, sans-serif;
    font-weight: 700;
    color: var(--brand-pink);
    letter-spacing: -1px;
    line-height: 1;
    white-space: nowrap;
  }
  .tagline {
    position: absolute;
    font-family: "Cabin", "Trebuchet MS", sans-serif;
    color: var(--tagline-grey);
    line-height: 1;
    white-space: nowrap;
  }

  /* front */
  .partner-badge {
    position: absolute;
    left: 28px; top: 22px;
    width: 58px; height: 62px;
    background: var(--badge-blue);
    border-radius: 6px;
  }
  .card--front .wordmark { left: 30px; top: 160px; font-size: 66px; }
  .card--front .tagline  { left: 32px; top: 234px; font-size: 26px; }
  .front-emblem {
    position: absolute;
    right: 30px; top: 40px;
    width: 170px; height: 170px;
    border-radius: 50%;
    background: var(--brand-pink);
  }

  /* back */
  .card--back .wordmark { left: 62px; top: 40px; font-size: 58px; }
  .card--back .tagline  { left: 64px; top: 104px; font-size: 22px; }
  .back-emblem {
    position: absolute;
    right: 30px; top: 80px;
    width: 130px; height: 130px;
    border-radius: 50%;
    background: var(--soft-pink);
  }
  .holder {
    position: absolute;
    left: 34px; top: 200px;
    padding-left: 16px;
    border-left: 6px solid var(--brand-green);
  }
  .holder__name {
    font-family: "Arimo", Arial, sans-serif;
    font-weight: 700;
    font-size: 26px;
    color: var(--brand-pink);
    letter-spacing: 0.5px;
    line-height: 40px;
  }
  .contact {
    position: absolute;
    font-family: "Arimo", Arial, sans-serif;
    font-size: 15px;
    line-height: 20px;
    color: var(--ink);
    white-space: nowrap;
  }
  .contact dt { display: inline; color: var(--brand-green); }
  .contact dd { display: inline; }
  .contact--reach { left: 50px; top: 262px; }
  .contact--place { left: 318px; top: 262px; }
  .contact .row { display: block; }
</style>
</head>
<body>
<main class="stage">

  <section class="card card--front" aria-label="Card front">
    <div class="partner-badge" role="img" aria-label="Certification badge"></div>
    <div class="wordmark">tealmarrow</div>
    <div class="tagline">Remedial and sports massage</div>
    <div class="front-emblem" role="img" aria-label="Brand emblem"></div>
  </section>

  <section class="card card--back" aria-label="Card back">
    <div class="wordmark">tealmarrow</div>
    <div class="tagline">Remedial and sports massage</div>
    <div class="back-emblem" role="img" aria-label="Faint brand emblem"></div>

    <div class="holder">
      <p class="holder__name">TALVINA BRISK</p>
    </div>

    <dl class="contact contact--reach">
      <div class="row"><dt>Call, SMS or ChatBeam:</dt> <dd>8317 6092</dd></div>
      <div class="row"><dt>Email:</dt> <dd>tealmarrow@quenfold.com</dd></div>
    </dl>
    <dl class="contact contact--place">
      <div class="row"><dt>Address:</dt> <dd>The Harbourview at Dunmore</dd></div>
      <div class="row"><dd>82 Dunmore Road, East Coast, Singapore</dd></div>
    </dl>
  </section>

</main>
</body>
</html>
```